Corporate travel agency website design

Hello I need a website design that will look professional. I want that anyone that gos on our site understands that we are a large successful company. I want it to be up to par with other large companies. The site should be sleek and neat.
Below I will attach my logo. A recent one page add I made and content for my add that will be used for the website.

```html
<!DOCTYPE html>
<html lang="en">
<head>
<meta charset="utf-8">
<title>Meridian Travel — Business Travel Reinvented</title>
<link rel="stylesheet" href="https://fonts.googleapis.com/css2?family=Montserrat:wght@400;500;600;700;800&family=Poppins:wght@300;400;500&display=swap">
<style>
:root{
  --navy:#0a1a3a;
  --navy-deep:#071431;
  --sky:#d1eefa;
  --sky-soft:#e6f6fc;
  --card:#f5f8fa;
  --ink:#1d2438;
  --muted:#3d4454;
  --line:#dfe5ea;
  --white:#ffffff;
}
*{margin:0;padding:0;box-sizing:border-box}
html,body{width:1200px;height:2843px;overflow:hidden;background:var(--white)}
body{position:relative;font-family:'Poppins',sans-serif;color:var(--ink)}
.abs{position:absolute}

/* top bar */
.topbar{left:0;top:0;width:1200px;height:41px;background:#f7f8fa}
.call{left:623px;top:11px;font:600 10px 'Montserrat',sans-serif;letter-spacing:.5px;color:var(--navy)}
.call strong{font-size:14px;font-weight:600;margin-left:3px}
.search{left:835px;top:0;width:255px;height:41px;background:var(--navy);color:#cfd6e4;font-size:10px;padding:13px 30px}
.search svg{position:absolute;right:14px;top:11px}
.navbar{left:0;top:41px;width:1200px;height:66px;background:rgba(255,255,255,.95)}
.nav{right:298px;top:68px;display:flex;font:500 11px 'Montserrat',sans-serif;letter-spacing:.4px;color:var(--muted);white-space:nowrap}
.nav span{padding:0 13px;border-left:1px solid #c9cfd8}
.nav span:first-child{border:0;padding-left:0;color:var(--navy);font-weight:600}
.nav span:last-child{padding-right:0}
.login{left:942px;top:55px;width:148px;height:37px;border:1px solid var(--line);background:var(--white);font:700 11px 'Montserrat',sans-serif;color:var(--navy);text-align:center;line-height:35px;letter-spacing:.4px}
.brand{left:110px;top:0;width:166px;height:134px;background:var(--navy);color:var(--white);text-align:center;z-index:3}
.brand-mark{display:block;margin:30px auto 0;width:28px;height:28px;border:1.3px solid #fff}
.brand-name{font:400 13px 'Montserrat',sans-serif;letter-spacing:1.5px;margin-top:24px}
.brand-tag{font:400 5px 'Montserrat',sans-serif;letter-spacing:2.6px;margin-top:3px}

/* hero */
.hero{left:0;top:107px;width:1200px;height:580px}
.hero-title{left:111px;top:270px;font:800 43px/45px 'Montserrat',sans-serif;color:var(--navy);letter-spacing:.5px}
.hero-sub{left:111px;top:368px;font:600 14px/18px 'Montserrat',sans-serif;letter-spacing:2px;color:var(--navy)}
.btn{display:flex;align-items:center;justify-content:center;gap:7px;background:var(--navy);color:var(--white);font:700 11px 'Montserrat',sans-serif;letter-spacing:.3px;outline:1px solid var(--navy);outline-offset:2px;border:1px solid rgba(255,255,255,.35)}
.hero-btn{left:110px;top:431px;width:156px;height:45px}

/* about & why */
.jet{left:0;top:980px;width:1200px;height:395px;background:linear-gradient(160deg,#e9eef2 0%,#f6f8fa 30%,#cdd3da 55%,#2a3340 78%,#b9c0c8 100%)}
.about-title{left:111px;top:790px;font:700 27px 'Montserrat',sans-serif;color:var(--navy)}
.about-text{left:111px;top:862px;width:400px;font:400 12.2px/19px 'Poppins',sans-serif;color:var(--muted)}
.about-btn{left:110px;top:947px;width:156px;height:46px}
.why{left:580px;top:620px;width:510px;height:600px;background:var(--sky);border-bottom:4px solid var(--navy);text-align:center}
.why-icon{display:block;margin:50px auto 0;width:75px;height:71px;background:var(--navy)}
.why h2{font:700 23px 'Montserrat',sans-serif;color:var(--navy);margin-top:12px}
.rule{width:56px;height:2px;background:var(--navy);margin:10px auto 0}
.why p{font:400 12.1px/19.3px 'Poppins',sans-serif;color:var(--muted);width:410px;margin:22px auto 0}
.why p+p{margin-top:18px}
.why-btn{left:177px;top:495px;width:156px;height:46px}

/* services */
.svc-title{left:0;top:1436px;width:1200px;text-align:center;font:700 27px 'Montserrat',sans-serif;color:var(--navy)}
.svc-rule{left:577px;top:1479px;width:46px;height:2px;background:#bfe6f5}
.card{top:1560px;width:318px;background:var(--card);border:1px solid #e6ebef;text-align:center}
.card.feature{border-bottom:4px solid var(--navy)}
.badge{position:absolute;left:121px;top:-38px;width:76px;height:76px;border-radius:50%;background:var(--sky);box-shadow:0 0 0 6px #fff;display:flex;align-items:center;justify-content:center}
.card h3{font:600 18px/18px 'Montserrat',sans-serif;color:var(--navy);margin-top:76px;letter-spacing:.3px}
.card p{font:400 11.4px/18.2px 'Poppins',sans-serif;color:var(--muted);width:262px;margin:22px auto 0}

/* highlights */
.band{left:0;top:2153px;width:1200px;height:690px;background:var(--sky)}
.tiles{left:110px;top:2225px;display:flex;gap:11px}
.tile{width:187px;height:136px;background:var(--white);text-align:center;padding-top:28px;font:500 13px/14px 'Poppins',sans-serif;color:var(--navy)}
.tile svg{display:block;margin:0 auto 12px}

/* footer */
.footer-shape{left:0;top:2400px}
.f-logo{left:220px;top:2578px;width:248px;text-align:center;color:var(--white)}
.f-mark{display:block;margin:20px auto 0;width:40px;height:40px;border:1.6px solid #fff}
.f-logo .name{font:400 17px 'Montserrat',sans-serif;letter-spacing:2.5px;margin-top:28px}
.f-logo .tag{font:400 7.5px 'Montserrat',sans-serif;letter-spacing:3.6px;margin-top:3px}
.socials{left:276px;top:2709px;display:flex;gap:11px}
.socials span{width:26px;height:26px;border:1px solid #3a4a6a}
.socials span.on{background:var(--white);border-color:var(--white)}
.vline{top:2590px;width:1px;height:146px;background:#2a3a5c}
.f-head{top:2574px;font:500 13px 'Montserrat',sans-serif;color:var(--white);letter-spacing:.4px}
.f-head::after{content:"";display:block;width:104px;height:1px;background:#3a4a6a;margin-top:10px}
.f-head::before{content:"";position:absolute;left:0;top:25px;width:18px;height:1px;background:#9fd8ef}
.contact{left:544px;font:400 11px/14px 'Poppins',sans-serif;color:#d6dcea;display:flex;gap:8px;align-items:flex-start}
.contact.phone{font:600 12.5px 'Montserrat',sans-serif;color:var(--white)}
.contact a{color:#d6dcea}
.links{left:836px;top:2626px;font:400 10.8px 'Poppins',sans-serif;color:#d6dcea;letter-spacing:.3px}
.links div{height:24.5px}
.f-rule{left:210px;top:2779px;width:780px;height:1px;background:#1e2e50}
.copy{left:0;top:2803px;width:1200px;text-align:center;font:400 11px 'Poppins',sans-serif;color:#c4cbda}
</style>
</head>
<body>

<!-- header -->
<div class="abs topbar"></div>
<div class="abs call">CALL US TODAY:- <strong>555-010-2040</strong></div>
<div class="abs search">Search...
  <svg width="20" height="20" viewBox="0 0 20 20" fill="none" stroke="#fff" stroke-width="1.4"><circle cx="8.5" cy="8.5" r="6.5"/><path d="M13.5 13.5L18 18"/></svg>
</div>

<!-- hero photo -->
<svg class="abs hero" viewBox="0 0 1200 580" role="img" aria-label="Businessman in a suit walking with a rolling suitcase through a bright airport terminal">
  <defs>
    <linearGradient id="heroFill" x1="0" y1="0" x2="1" y2="0">
      <stop offset="0" stop-color="#eef3f7"/>
      <stop offset=".45" stop-color="#dfe8ef"/>
      <stop offset=".6" stop-color="#5f6f86"/>
      <stop offset=".75" stop-color="#c9d6e0"/>
      <stop offset="1" stop-color="#8c9cae"/>
    </linearGradient>
  </defs>
  <polygon points="0,0 1200,0 1200,560 1080,515 580,515 0,573" fill="url(#heroFill)"/>
  <polygon points="0,573 580,508 1080,490 1200,545 1200,565 1080,520 580,522" fill="var(--navy)"/>
</svg>

<div class="abs navbar"></div>
<nav class="abs nav"><span>HOME</span><span>ABOUT US</span><span>SOLUTIONS</span><span>WHY MERIDIAN TRAVEL</span><span>RESOURCES</span></nav>
<div class="abs login">TRAVELER LOGIN</div>

<div class="abs brand">
  <span class="brand-mark"></span>
  <div class="brand-name">MERIDIAN TRAVEL</div>
  <div class="brand-tag">BUSINESS TRAVEL REINVENTED</div>
</div>

<h1 class="abs hero-title">BUSINESS<br>TRAVEL REINVENTED</h1>
<p class="abs hero-sub">MERIDIAN TRAVEL IS A GLOBAL LEADER IN BUSINESS<br>TRAVEL MANAGEMENT SERVICES.</p>
<div class="abs btn hero-btn">
  <svg width="20" height="18" viewBox="0 0 20 18" fill="none" stroke="#fff" stroke-width="1.6"><path d="M3 11V9a7 7 0 0114 0v2"/><rect x="1.5" y="10" width="3.5" height="6" rx="1"/><rect x="15" y="10" width="3.5" height="6" rx="1"/></svg>
  TALK TO US
</div>

<!-- about -->
<div class="abs jet" role="img" aria-label="White private jet parked on an airport apron"></div>
<div class="abs" style="left:0;top:930px;width:600px;height:80px;background:linear-gradient(#fff,rgba(255,255,255,0))"></div>
<h2 class="abs about-title">ABOUT MERIDIAN TRAVEL</h2>
<p class="abs about-text">Meridian Travel is a global leader in business travel management services. We drive savings, efficiency, and unparalleled service to businesses and their travelers all around the world.</p>
<div class="abs btn about-btn">LEARN MORE</div>

<section class="abs why">
  <span class="why-icon"></span>
  <h2>WHY CHOOSE MERIDIAN TRAVEL?</h2>
  <div class="rule"></div>
  <p>Meridian Travel is a global leader in business travel management services. We drive savings, efficiency, and unparalleled service to businesses and their travelers all around the world.</p>
  <p>If you are looking for a tailored travel managed solution focused on offering white glove service and fulfilling your individual preferences ,while delivering customer excellence, you've come to the right place. At Meridian Travel, our mission is to have you focus on your day to day business while we handle all of the logistics and details for the most successful all encompassing travel experience. From emergency passport arrangements to last minute cancellations, re-bookings, and other intricate travel challenges, Meridian Travel is well versed in handling the routine array of travel services, as well as solving any travel related issue that might arise.</p>
  <div class="abs btn why-btn">
    <svg width="20" height="18" viewBox="0 0 20 18" fill="none" stroke="#fff" stroke-width="1.6"><path d="M3 11V9a7 7 0 0114 0v2"/><rect x="1.5" y="10" width="3.5" height="6" rx="1"/><rect x="15" y="10" width="3.5" height="6" rx="1"/></svg>
    TALK TO US
  </div>
</section>

<!-- services -->
<h2 class="abs svc-title">TRAVEL MANAGEMENT SERVICE</h2>
<div class="abs svc-rule"></div>

<article class="abs card" style="left:110px;height:373px">
  <div class="badge"><svg width="40" height="40" viewBox="0 0 40 40" fill="none" stroke="var(--navy)" stroke-width="2.2"><circle cx="22" cy="13" r="8"/><path d="M22 8v10M19.5 10.5h4a1.5 1.5 0 010 3h-3a1.5 1.5 0 000 3h4"/><path d="M4 26h6l6 2h7a2 2 0 010 4h-6M10 36h12l12-8"/></svg></div>
  <h3>UNPARALLED<br>SERVICE</h3>
  <p>Meridian Travel Is Famous For Our Concierge Style Approach To Travel. From Detailed Planning, To Commercial Or Private Air Travel, Transportation, Including Car Rentals, Chauffers, Busses For Larger Groups, Hotels, All Styles Of Lodging Accomodations, Special Event Planning And More, Meridian Travel Is Like Having Your Own Personal Or Corporate Travel Butler.</p>
</article>

<article class="abs card feature" style="left:440px;height:516px">
  <div class="badge"><svg width="42" height="42" viewBox="0 0 42 42" fill="none" stroke="var(--navy)" stroke-width="2"><circle cx="13" cy="9" r="6"/><rect x="7" y="17" width="16" height="20"/><rect x="22" y="22" width="14" height="16" fill="var(--navy)"/><path d="M11 33v-4M15 33v-7M19 33v-9"/></svg></div>
  <h3>BUDGET &amp; TRAVEL<br>SPEND REPORTING</h3>
  <p>Having a travel management service will ensure that your company enforces corporate compliance and maintains control over travel decisions. This ensures that your employees stick to your budget, which in turn will protect your bottom line. Travel expenses can be costly. Having a savvy and experienced corporate travel manager who can access deep discounts not available to the public will ensure your travel is booked across the board at the lowest prices expenses are kept under control. Travel reporting is critical to optimizing budgets, streamlining expense reports, and recognizing key trends. Meridian-Travel customizes travel spend reports, by team, project, department etc, so companies can accurately track travel expenses, and make critical decisions based on the spend.</p>
</article>

<article class="abs card" style="left:772px;height:453px">
  <div class="badge"><svg width="44" height="44" viewBox="0 0 44 44" fill="none" stroke="var(--navy)" stroke-width="2.6"><path d="M36 14a17 17 0 11-6-6"/><path d="M30 4v5h5"/><circle cx="22" cy="23" r="11" fill="var(--navy)"/><path d="M22 16v7l4 3" stroke="#fff" stroke-width="2"/></svg></div>
  <h3>EFFICIENCY</h3>
  <p style="margin-top:40px">Time is your most valuable tool! Our goal at Meridian Travel is to have your employees' complete focus be on your core business, while having us handle all the logistics for their travel. One of the most appreciated services we offer is the management of travel headaches. Unforeseen circumstances such as cancellations, missed flights, cancelled flights, last minute bookings or changed plans, can take hours to rectify. Meridian Travel handles all of these tedious repositionings expeditiously, saving your employees precious time. Give your company a competitive edge by having Meridian Travel handle your team's travel arrangements.</p>
</article>

<!-- highlights -->
<div class="abs band"></div>
<div class="abs tiles">
  <div class="tile"><svg width="40" height="40" viewBox="0 0 40 40" fill="none" stroke="var(--navy)" stroke-width="1.4"><path d="M8 36V20l3-8 3 6V10l3 8 2-6v24zM21 36V18l3-6 3 6V12l3 6 3-4v22z"/><path d="M10 4l2 3M16 2v3M4 9l3 1"/></svg>Whith<br>Glove Service</div>
  <div class="tile"><svg width="40" height="40" viewBox="0 0 40 40" fill="none" stroke="var(--navy)" stroke-width="1.4"><rect x="6" y="12" width="20" height="24"/><path d="M10 18h12M10 23h12M10 28h8"/><circle cx="29" cy="10" r="7"/><path d="M26 10l2 2 4-4"/></svg>Corporate Travel<br>Policy Compliance</div>
  <div class="tile"><svg width="40" height="40" viewBox="0 0 40 40" fill="none" stroke="var(--navy)" stroke-width="1.4"><rect x="9" y="3" width="22" height="34"/><path d="M13 9h14M13 13h10M14 32v-6M19 32v-9M24 32v-12M28 32v-4"/></svg>Streamlined<br>Expense Reports</div>
  <div class="tile"><svg width="40" height="40" viewBox="0 0 40 40" fill="none" stroke="var(--navy)" stroke-width="1.6"><path d="M5 5h26l4 4v26H5z"/><rect x="11" y="5" width="16" height="10"/><rect x="10" y="22" width="20" height="13"/></svg>Unparalleled<br>Savings</div>
  <div class="tile"><svg width="40" height="40" viewBox="0 0 40 40" fill="none" stroke="var(--navy)" stroke-width="1.4"><circle cx="16" cy="11" r="5"/><circle cx="16" cy="11" r="2"/><circle cx="31" cy="6" r="3"/><circle cx="31" cy="16" r="3"/><path d="M3 28h7l6 2h6a2 2 0 010 4h-5M10 36h12l13-9"/></svg>Full Service<br>Travel Management</div>
</div>

<!-- footer -->
<svg class="abs footer-shape" width="1200" height="443" viewBox="0 0 1200 443">
  <polygon points="0,117 221,29 1200,150 1200,443 0,443" fill="var(--navy-deep)"/>
  <polygon points="0,117 221,29 221,22" fill="#f4fbfe"/>
</svg>

<div class="abs f-logo">
  <span class="f-mark"></span>
  <div class="name">MERIDIAN TRAVEL</div>
  <div class="tag">BUSINESS TRAVEL REINVENTED</div>
</div>
<div class="abs socials"><span></span><span class="on"></span><span></span><span></span></div>

<div class="abs vline" style="left:485px"></div>
<div class="abs vline" style="left:773px"></div>

<div class="abs f-head" style="left:545px">CONTACT US</div>
<div class="abs contact" style="top:2627px">
  <svg width="12" height="16" viewBox="0 0 12 16" fill="#fff"><path d="M6 0a6 6 0 00-6 6c0 4.5 6 10 6 10s6-5.5 6-10a6 6 0 00-6-6zm0 8.5A2.5 2.5 0 116 3.5a2.5 2.5 0 010 5z"/></svg>
  <span>Location name will be here<br>near this building 12345</span>
</div>
<div class="abs contact phone" style="top:2681px">
  <svg width="16" height="16" viewBox="0 0 16 16" fill="#fff"><path d="M3.5 1l2.5 3-1.5 2a9 9 0 005 5l2-1.5 3 2.5-1.5 2.5C7 15 1 9 1 2.5z"/></svg>
  555-010-2040
</div>
<div class="abs contact" style="top:2725px">
  <svg width="14" height="11" viewBox="0 0 14 11" fill="none" stroke="#fff" stroke-width="1.2"><rect x=".6" y=".6" width="12.8" height="9.8"/><path d="M.6.6L7 6l6.4-5.4"/></svg>
  <a href="#">info@meridiantravel.com</a>
</div>

<div class="abs f-head" style="left:835px">QUICK LINKS</div>
<div class="abs links">
  <div>HOME</div><div>ABOUT US</div><div>WHY CHOOSE US</div><div>RESOURCES</div><div>CONTACT</div>
</div>

<div class="abs f-rule"></div>
<div class="abs copy">©2023 meridiantravel.com | All Rights Reserved.</div>

</body>
</html>
```